English and Spanish Language School Needs a Business Card

Need a business card design a startup company called Corvelle Language School. The company will offer English and Spanish conversational level courses designed to make the learner feel comfortable with grammar and vocabulary. We would like to see a logo with some colour that should communicate learning, growth.

Target Market(s)

Consumers and businesses

Industry/Entity Type

Education

Contact Information for Business Card

TBD

Font styles to use
Serif

Requirements
Must have
• Include the following
• Logo
• Name
• Title
• Cellphone Number
• Office Phone number
• Email address
• Office Address

```html
<!DOCTYPE html>
<html lang="en">
<head>
<meta charset="utf-8">
<title>Corvelle Language School — Business Card</title>
<link href="https://fonts.googleapis.com/css2?family=Open+Sans:wght@400;600;700&display=swap" rel="stylesheet">
<style>
  :root {
    --backdrop: #ececec;
    --card-white: #fbfbfb;
    --brand-red: #c4222a;
    --ink-grey: #555555;
    --ink-dark: #333333;
    --paper-white: #ffffff;
  }
  * { box-sizing: border-box; margin: 0; padding: 0; }
  html, body {
    width: 1200px;
    height: 900px;
    overflow: hidden;
    background: var(--backdrop);
    font-family: "Open Sans", Arial, sans-serif;
  }
  .card-sheet {
    position: relative;
    width: 1200px;
    height: 900px;
    display: flex;
    align-items: center;
    justify-content: center;
    gap: 40px;
  }
  .card {
    width: 540px;
    height: 309px;
    position: relative;
    box-shadow: 0 2px 6px rgba(0,0,0,0.12);
  }
  .card--front { background: var(--card-white); }
  .card--back {
    background: var(--brand-red);
    display: flex;
    align-items: center;
    justify-content: center;
  }
  .wordmark {
    font-weight: 700;
    line-height: 1.05;
    letter-spacing: -0.5px;
  }
  .card--front .wordmark {
    position: absolute;
    top: 52px;
    left: 200px;
    color: var(--brand-red);
    font-size: 30px;
  }
  .card--back .wordmark {
    color: var(--paper-white);
    font-size: 40px;
    text-align: left;
  }
  .contact-block {
    position: absolute;
    top: 148px;
    right: 150px;
    text-align: right;
    font-size: 12px;
    line-height: 1.45;
    color: var(--ink-grey);
  }
  .contact-block .person-name {
    color: var(--brand-red);
    font-weight: 600;
    font-size: 15px;
    letter-spacing: 0.5px;
  }
  .contact-block .person-title { margin-bottom: 2px; }
  .contact-block .label {
    color: var(--brand-red);
    font-weight: 600;
  }
  .contact-block .address {
    color: var(--ink-dark);
    margin-top: 1px;
  }
</style>
</head>
<body>
  <main class="card-sheet">
    <section class="card card--front" aria-label="Business card front">
      <div class="wordmark">Corvelle<br>Language School</div>
      <div class="contact-block">
        <div class="person-name">MARTA QUILLON</div>
        <div class="person-title">Managing Director</div>
        <div><span class="label">P:</span> 823-555-0147</div>
        <div><span class="label">M:</span> 823-555-0198</div>
        <div><span class="label">E:</span> hello@corvelle-school.com</div>
        <div class="address">48, Linden Row, Harrowgate, Country, 204816</div>
      </div>
    </section>
    <section class="card card--back" aria-label="Business card back">
      <div class="wordmark">Corvelle<br>Language School</div>
    </section>
  </main>
</body>
</html>
```